Summer Fun

I need a Poster for Front of hotel advertising discounted drinks on Thursday & Fridays
$3.50.
Schooners of Local Beer, Glass of House Wine & Bubbly.
From 3.30pm to 6.30 pm
Nibblies Provided

25 + Market

Hotel

• Do not want to be known as Happy Hour.

```html
<!DOCTYPE html>
<html lang="en">
<head>
<meta charset="utf-8">
<title>Summer Offers</title>
<link rel="stylesheet" href="https://fonts.googleapis.com/css2?family=Courgette&family=Merienda:wght@400;500&display=swap">
<style>
  :root {
    --paper: #ffffff;
    --ink: #111111;
    --berry: #d4145f;
    --lager: #fbe49b;
    --lager-soft: #fdf0c8;
    --badge: #0b0b0b;
    --badge-text: #ffffff;
  }
  * { margin: 0; padding: 0; box-sizing: border-box; }
  html, body { width: 849px; height: 1200px; overflow: hidden; background: var(--paper); }
  .poster {
    position: relative;
    width: 849px;
    height: 1200px;
    background: var(--paper);
    overflow: hidden;
  }
  .drinks-art {
    position: absolute;
    left: 100px;
    top: 0;
    width: 690px;
    height: 1200px;
    background: linear-gradient(180deg, var(--lager-soft) 0%, var(--lager) 55%, var(--lager-soft) 100%);
  }
  .headline {
    position: absolute;
    top: 22px;
    left: 0;
    width: 100%;
    text-align: center;
    font-family: "Merienda", cursive;
    font-size: 84px;
    font-weight: 400;
    line-height: 110px;
    color: var(--ink);
    letter-spacing: 2px;
    white-space: nowrap;
  }
  .offer {
    position: absolute;
    left: 0;
    width: 100%;
    text-align: center;
    font-family: "Courgette", cursive;
    color: var(--berry);
    white-space: nowrap;
  }
  .offer--beer { top: 192px; font-size: 72px; line-height: 90px; }
  .offer--wine { top: 322px; font-size: 72px; line-height: 76px; }
  .offer--price { top: 520px; font-size: 112px; line-height: 140px; }
  .days {
    position: absolute;
    top: 716px;
    left: 118px;
    width: 600px;
    text-align: center;
    font-family: "Merienda", cursive;
    font-size: 58px;
    line-height: 68px;
    color: var(--ink);
    white-space: nowrap;
  }
  .hours {
    position: absolute;
    top: 918px;
    left: 50px;
    width: 470px;
    font-family: "Merienda", cursive;
    font-size: 60px;
    line-height: 76px;
    color: var(--ink);
    white-space: nowrap;
  }
  .hours span { display: block; }
  .hours .line-start { padding-left: 55px; }
  .hours .line-time { padding-left: 112px; }
  .hours .line-end { padding-left: 0; }
  .nibbles-badge {
    position: absolute;
    left: 515px;
    top: 857px;
    width: 286px;
    height: 286px;
    border-radius: 50%;
    background: var(--badge);
    display: flex;
    align-items: center;
    justify-content: center;
  }
  .nibbles-badge p {
    transform: rotate(20deg);
    text-align: center;
    font-family: "Merienda", cursive;
    font-size: 44px;
    line-height: 54px;
    color: var(--badge-text);
  }
</style>
</head>
<body>
  <main class="poster">
    <div class="drinks-art" role="img" aria-label="Illustration of a beer bottle beside a frothy glass of beer in pale yellow"></div>

    <h1 class="headline">Summer Offers</h1>

    <p class="offer offer--beer">Schooner of Local Beer</p>
    <p class="offer offer--wine">Glass of House Wine or<br>Bubbly</p>
    <p class="offer offer--price">All $3.50</p>

    <p class="days">Every Thursday<br>&amp; Friday</p>

    <p class="hours">
      <span class="line-start">Between</span>
      <span class="line-time">3.30pm</span>
      <span class="line-end">and&nbsp; 6.30pm</span>
    </p>

    <div class="nibbles-badge">
      <p>Nibbles<br>Also<br>Provided</p>
    </div>
  </main>
</body>
</html>
```